Frontpage for an independent Forex trading tournaments website

We need a frontpage design for the first independent Forex trading tournaments platform.
Intraday Forex traders from all over the world come to this website to participate in daily contests, and if they trade better than others — win the bets. This website is the first of a kind — it is not affiliated with any type of brokers, and does not promote any broker services.
People can trade with their existing live or demo accounts (and they even can win real money with demo accounts)
The main goal of the frontpage is to explain what this website is about and make them sign up via Vendrix or Lumora buttons, or traditional email.
Attached to this project is a sample mock-up that seems reasonable, but we're open to further suggestions.
Updates
Dear designers,
Also please use bigger fonts and use don't leave too big blank spaces.
Target Market(s)
Intraday Forex traders from 24 to 34 years, mostly males, higher education, working as traders or trading as a hobby.
Mostly living in developing countries: Indonesia, Eastern Europe, Arab countries, China, Latin America.
Industry/Entity Type
Trade
Requirements
Must have
- * Clean design with clear message
* An easy-to-see way to show that we have single-click Vendrix/Lumora registration
Should not have
- * No implied javascript-animated nested menus or pop-ups, no flash — that would make the website difficult to browse on mobile devices which employ touch-based controls

```html
<!DOCTYPE html>
<html lang="en">
<head>
<meta charset="utf-8">
<title>PipArena.com — Forex Tournaments</title>
<link rel="stylesheet" href="https://fonts.googleapis.com/css2?family=Open+Sans:wght@400;600;700&display=swap">
<style>
:root{
  --green:#6fa51c;
  --green-dark:#4f8410;
  --ink:#222;
  --dark:#2f2f2f;
  --row-line:#e2e2e2;
  --panel:#f1f1f1;
  --vendrix:#4a6aa5;
  --lumora:#37b3e6;
  --nexlink:#2f78b0;
  --feed:#ef8a22;
}
*{box-sizing:border-box;margin:0;padding:0}
html,body{width:885px;height:1200px;overflow:hidden}
body{position:relative;font-family:"Open Sans",Arial,sans-serif;color:var(--ink);background:#fff}
.abs{position:absolute}
.topbar{left:0;top:0;width:885px;height:6px;background:var(--green)}
.signin-tab{left:712px;top:5px;width:76px;height:18px;background:var(--green);color:#fff;font-size:9px;text-align:center;line-height:18px;border-radius:0 0 10px 10px}
.header{left:0;top:6px;width:885px;height:78px;background:#f7f7f7;border-bottom:1px solid #e6e6e6}
.logo{left:96px;top:36px;font-size:24px;letter-spacing:.5px;color:#2b2b2b}
.nav a{position:absolute;top:48px;font-size:9.5px;color:#333;text-decoration:none}
.join-btn{left:722px;top:38px;width:67px;height:23px;background:linear-gradient(#7cbb26,#558f12);color:#fff;font-size:8px;font-weight:600;text-align:center;line-height:23px;border:1px solid #4c7e12}
.hero{left:0;top:84px;width:885px;height:340px;background:radial-gradient(ellipse at 50% 60%,#fff 0%,#f0f0f0 70%,#e9e9e9 100%)}
.headline{left:60px;top:106px;width:765px;text-align:center;font-size:18.5px;line-height:25px;color:#222;font-weight:400}
.trader-photo{left:128px;top:180px;width:194px;height:244px;border-radius:90px 90px 0 0;background:linear-gradient(#d9cfc8 0%,#3b3b3b 45%,#2a2a2a 100%)}
.bubble{left:272px;top:186px}
.bubble-text{left:290px;top:204px;width:162px;font-size:7.4px;line-height:13.2px;color:#fff;text-align:justify}
.brokers{left:508px;top:194px;width:280px;height:204px;background:#fff;border:1px solid #e4e4e4;box-shadow:4px 8px 8px rgba(0,0,0,.15)}
.brokers h2{position:absolute;top:9px;width:100%;text-align:center;font-size:15px;font-weight:600;color:var(--green)}
.broker{position:absolute;width:120px;text-align:center;font-size:13px;font-weight:600;color:#333;display:flex;align-items:center;justify-content:center;gap:6px}
.broker i{display:inline-block;width:12px;height:12px;background:#888}
.dots{left:414px;top:406px;display:flex;gap:3px}
.dots span{width:12px;height:12px;border-radius:50%;background:#3a3a3a}
.dots span.off{background:#d0d0d0}
.section-title{left:97px;top:444px;font-size:12px;color:var(--green);font-weight:600}
.table-head{left:96px;top:466px;width:693px;height:35px;background:linear-gradient(#3d3d3d,#262626);color:#fff;font-size:9px}
.table-head span{position:absolute;top:12px}
.table-head span::before{content:"";display:inline-block;border:4px solid transparent;border-top:6px solid #fff;border-bottom:0;margin-right:6px;vertical-align:1px}
.row{position:absolute;left:96px;width:693px;height:35px;border-bottom:1px solid var(--row-line);font-size:9.5px;background:#fafafa}
.row .name{position:absolute;left:10px;top:11px;font-weight:600;color:#333}
.row .due{position:absolute;left:184px;top:11px;color:#444}
.row .prize{position:absolute;left:414px;top:11px;color:#222}
.row .fee{position:absolute;left:556px;top:7px;width:91px;height:21px;border-radius:4px;background:linear-gradient(#96cf45,#5f9a16);border:1px solid #4c7e12;color:#fff;font-weight:700;text-align:center;line-height:19px;font-size:9.5px}
.row .fee.free{background:linear-gradient(#5a5a5a,#333);border-color:#222;font-weight:600;font-size:9px}
.row .toggle{position:absolute;left:666px;top:9px;width:16px;height:16px;border-radius:50%;background:#333;color:#fff;text-align:center;line-height:15px;font-weight:700;font-size:12px}
.details{left:96px;top:678px;width:693px;height:104px;background:var(--panel);font-size:7.5px;color:#555}
.details span{position:absolute}
.rules-link{left:10px;top:85px;font-size:9px;color:#333;font-weight:600;text-decoration:underline}
.badge{left:96px;top:786px}
.signup{top:819px;height:28px;font-size:10.5px;font-weight:600;color:#fff;display:flex;align-items:center}
.signup .mark{width:28px;height:100%;display:flex;align-items:center;justify-content:center;border-right:1px solid rgba(255,255,255,.3);font-size:11px}
.signup .label{flex:1;text-align:center}
.signup.vendrix{left:213px;width:170px;background:linear-gradient(#5b7bb7,#3d5b94)}
.signup.lumora{left:390px;width:169px;background:linear-gradient(#52c3f0,#2aa3d8)}
.or{left:579px;top:825px;font-size:13px;color:#555}
.signup.email{left:618px;width:171px;background:linear-gradient(#444,#222);justify-content:center}
.footer{left:0;top:881px;width:885px;height:319px;background:var(--dark)}
.disclaimer-title{left:0;top:887px;width:885px;text-align:center;color:#fff;font-size:12px}
.footer-rule{left:0;top:906px;width:885px;height:1px;background:#444}
.disclaimer{left:94px;top:912px;width:700px;text-align:center;color:#fff;font-size:7.6px;line-height:13.3px}
.links a{position:absolute;color:#fff;font-size:7.6px;text-decoration:none}
.bottom-rule{left:0;top:1130px;width:885px;height:1px;background:#444}
.pay{top:1141px;display:flex;gap:6px;left:96px}
.pay span{width:26px;height:16px;background:#fff;border-radius:2px;font-size:5px;color:#333;display:flex;align-items:center;justify-content:center;font-weight:600}
.copyright{left:280px;top:1141px;width:300px;text-align:center;color:#fff;font-size:9.5px;line-height:18px}
.social{left:686px;top:1140px;display:flex;gap:10px}
.social span{width:18px;height:18px;color:#fff;font-size:10px;font-weight:700;display:flex;align-items:center;justify-content:center}
</style>
</head>
<body>
<div class="abs topbar"></div>
<div class="abs header"></div>
<div class="abs signin-tab">Sign In</div>
<div class="abs logo"><span style="color:var(--green)">Pip</span>Arena.com</div>
<nav class="nav">
  <a style="left:502px" href="#">Tournaments</a>
  <a style="left:586px" href="#">Winners</a>
  <a style="left:650px" href="#">Q&amp;A</a>
</nav>
<div class="abs join-btn">Join Now</div>

<section class="abs hero"></section>
<h1 class="abs headline">Over 30,000 traders from all over the world have joined PipArena.com to participate in broker-independent real-money forex tournaments</h1>
<div class="abs trader-photo" role="img" aria-label="Photo of a smiling trader in a dark business suit, arms crossed"></div>
<svg class="abs bubble" width="200" height="140" viewBox="0 0 200 140" aria-hidden="true">
  <path d="M18 0 H179 Q197 0 197 18 V80 Q197 98 179 98 H70 L16 138 L40 98 H18 Q0 98 0 80 V18 Q0 0 18 0Z" fill="#78b72a"/>
</svg>
<p class="abs bubble-text">I have been participating in the tournaments for three months already, and I can't even find right words to express my passion for forex trading and excitement I get from fairly competing with people who feel the same</p>

<aside class="abs brokers">
  <h2>Broker Trust Us</h2>
  <div class="broker" style="left:18px;top:52px"><i style="background:#e36b2c;border-radius:50%"></i>Northbay</div>
  <div class="broker" style="left:142px;top:52px"><i style="background:#d2232a"></i>Kerrow Trade</div>
  <div class="broker" style="left:18px;top:112px"><i style="background:#333"></i>Orin Brokers</div>
  <div class="broker" style="left:142px;top:112px"><i style="background:#5ba732;border-radius:50%"></i>Valtrix</div>
  <div class="broker" style="left:18px;top:164px"><i style="background:#59a83a;border-radius:50%"></i>Tradeza</div>
  <div class="broker" style="left:142px;top:164px"><i style="background:#222"></i>Halden FX</div>
</aside>
<div class="abs dots"><span></span><span></span><span></span><span class="off"></span></div>

<h2 class="abs section-title">Soonest Tournaments</h2>
<div class="abs table-head">
  <span style="left:22px">Name</span>
  <span style="left:184px">Due</span>
  <span style="left:396px">1st Prize</span>
  <span style="left:570px">Join Now</span>
</div>
<div class="row" style="top:502px"><span class="name">Double or Nothing Thirty</span><span class="due">in 24m</span><span class="prize">$ 60</span><span class="fee">$33</span><span class="toggle">+</span></div>
<div class="row" style="top:537px"><span class="name">Regular European Ten</span><span class="due">in 4h 24m</span><span class="prize">$ 90</span><span class="fee">$11</span><span class="toggle">+</span></div>
<div class="row" style="top:572px"><span class="name">Lucky European Freeoil</span><span class="due">in 4h 24m</span><span class="prize">$ 15</span><span class="fee free">FREE</span><span class="toggle">+</span></div>
<div class="row" style="top:607px"><span class="name">Regular American Ten</span><span class="due">in 7h 24m</span><span class="prize">$100</span><span class="fee">$11</span><span class="toggle">+</span></div>
<div class="row" style="top:642px;height:36px"><span class="name">World Cup</span><span class="due">in 3 months</span><span class="prize">$ 300 000</span><span class="fee">$100</span><span class="toggle">−</span></div>
<div class="abs details">
  <span style="left:10px;top:12px">Prize Fund</span><span style="left:99px;top:12px">$ 300 000</span>
  <span style="left:186px;top:11px">Registration Ends</span><span style="left:414px;top:11px">15 Nov 2013, 17:00 GMT</span>
  <span style="left:10px;top:38px">Participants</span><span style="left:99px;top:38px">241 (max.10000)</span>
  <span style="left:186px;top:37px">Trading Starts</span><span style="left:414px;top:37px">20 Dec 2013, 17:00 GMT</span>
  <span style="left:10px;top:65px">Participants Fee</span><span style="left:99px;top:65px">$100</span>
  <span style="left:186px;top:63px">Trading Ends</span><span style="left:414px;top:63px">20 Dec 2013, 17:00 GMT</span>
  <a class="abs rules-link" href="#">World Cup Tournament Rules</a>
</div>

<svg class="abs badge" width="82" height="82" viewBox="0 0 82 82" role="img" aria-label="100% deposit bonus in April">
  <ellipse cx="41" cy="78" rx="34" ry="3" fill="#ddd"/>
  <polygon points="41,2 51,28 79,29 57,46 65,74 41,58 17,74 25,46 3,29 31,28" fill="#5d9a1a" stroke="#4a7f12"/>
  <text x="41" y="38" text-anchor="middle" fill="#fff" font-family="Open Sans,sans-serif" font-size="11" font-weight="700">100%</text>
  <text x="41" y="48" text-anchor="middle" fill="#fff" font-family="Open Sans,sans-serif" font-size="8" font-weight="600">Deposit</text>
  <text x="41" y="55" text-anchor="middle" fill="#fff" font-family="Open Sans,sans-serif" font-size="4.5">Bonus in April</text>
</svg>
<a class="abs signup vendrix"><span class="mark">V</span><span class="label">Enter With Vendrix</span></a>
<a class="abs signup lumora"><span class="mark">L</span><span class="label">Enter with Lumora</span></a>
<div class="abs or">(or)</div>
<a class="abs signup email">Register With Good Old E-Mail</a>

<footer class="abs footer"></footer>
<div class="abs disclaimer-title">Disclaimer</div>
<div class="abs footer-rule"></div>
<p class="abs disclaimer">The material in this web site is provided for entertainment and informational purposes only. Information offered may not be used to violate the local, state, regional or federal laws of any country. You must consult your local authorities for laws that may apply to you. This site does not encourage you to get or engage in gambling. Any use of this information in violation of local, state, regional, or federal laws of any country is prohibited.</p>
<div class="links">
  <a style="left:155px;top:973px" href="#">Home</a>
  <a style="left:155px;top:999px" href="#">Tournaments</a>
  <a style="left:155px;top:1026px" href="#">Winners</a>
  <a style="left:155px;top:1052px" href="#">Q&amp;A</a>
  <a style="left:155px;top:1079px" href="#">Register</a>
  <a style="left:155px;top:1105px" href="#">Sign In</a>
  <a style="left:272px;top:973px" href="#">Win with Demo Accounts</a>
  <a style="left:272px;top:999px" href="#">100% Deposit Bonus</a>
  <a style="left:272px;top:1026px" href="#">Guaranteed prize Fund</a>
  <a style="left:272px;top:1052px" href="#">Earn With friends</a>
  <a style="left:390px;top:973px" href="#">Tournaments Rules</a>
  <a style="left:390px;top:999px" href="#">Client Agreement</a>
  <a style="left:390px;top:1026px" href="#">Privacy</a>
  <a style="left:509px;top:973px" href="#">About PipArena.com</a>
  <a style="left:509px;top:999px" href="#">Licenses and Documents</a>
  <a style="left:509px;top:1026px" href="#">Press Contacts</a>
  <a style="left:509px;top:1052px" href="#">Partnership proposal</a>
</div>
<div class="abs bottom-rule"></div>
<div class="abs pay">
  <span>Tavo</span><span>Cardia</span><span>Mavrin</span><span>Circa</span><span>Amplo</span><span>Penwy</span>
</div>
<div class="abs copyright">Copyright(c) 2011-2013 PipArena.com, All rights reserved<br>English &nbsp;|&nbsp; español &nbsp;|&nbsp; русский &nbsp;|&nbsp; Indonesia &nbsp;|&nbsp; 中国的</div>
<div class="abs social">
  <span style="background:var(--vendrix)" aria-label="Vendrix">V</span>
  <span style="background:var(--lumora)" aria-label="Lumora">L</span>
  <span style="background:var(--nexlink)" aria-label="Nexlink">N</span>
  <span style="background:var(--feed)" aria-label="News feed">F</span>
</div>
</body>
</html>
```